Zielgruppe
Wir sind ein Vertriebsunternehmen, mit dem Ziel die klassische Finanz und den Kryptosektor zu verbinden. Unsere Zielgruppe sind Menschen zwischn 25 - 45 Jahre.
Aufgabenstellung
Wir sind ein Vertriebsunternehmen, mit dem Ziel die klassische Finanz und den Kryptosektor zu verbinden. Unsere Zielgruppe sind Menschen zwischn 25 - 45 Jahre. Wir sind die Communty und Vertrieb der ersten rechtkonformen STO - Plattform ( Plattform für Wertpapiere im Kryptosektor)
Diese Projekt ist Teil eines Paketes, wir bitten nur Designer mit zu machen die alle benötigten Unterlagen designen können.
Online-Marketing Material
2 Vorlagen Social Media - (Einladung/Event, Sprüche/Information)
Banner
Präsentationsvorlagen - min unterschiedliche 8 Vorlagenseiten /Layouts.
Landingpage Layout f. Funnelsite für Webinaranmeldung mit Platz für Formular
Newsletter Layoutvorlage
Vorlage Infografik
Broschüre / E - Book Designe
Es werden nur Vorlagen benötigt mit 'LoremSum Texten' und Musterbildern. Wir möchten von allen Vorlagen die Originaldatei, uns stehen folgende Grafikprogramme zur Verfügung:
Adobe Photoshop
Adobe Illustrator
Canva
Unsere Akt. Designe (Designe Alt) gefällt uns von der Idee, dennoch wünschen wir es uns moderner und edler mit ein wenig 'spaceig'. - Eben die Vereinigung von Kryptowelt und klassischer Finanz.
Schriftart: Poppins
Farben lt. Logo

```html
<!DOCTYPE html>
<html lang="de">
<head>
<meta charset="utf-8">
<title>Präsentationsvorlagen</title>
<link href="https://fonts.googleapis.com/css2?family=Poppins:wght@400;500;600;700;800;900&display=swap" rel="stylesheet">
<style>
:root{
  --stage:#1f1f21;
  --navy:#061638;
  --deep:#0a2a78;
  --blue:#1556c9;
  --bright:#2d8cf0;
  --cyan:#14b8f5;
  --white:#ffffff;
  --ink:#111111;
  --title-top:#5aa7dc;
  --title-bottom:#1a4fb0;
}
*{margin:0;padding:0;box-sizing:border-box}
html,body{width:1200px;height:848px;overflow:hidden;background:var(--stage)}
body{font-family:"Poppins",sans-serif;position:relative;
  background:radial-gradient(ellipse at 50% 40%,#2a2a2d 0%,var(--stage) 70%)}
.slide{position:absolute;overflow:hidden;box-shadow:0 6px 18px rgba(0,0,0,.55)}
.tech-bg{position:absolute;inset:0;
  background:radial-gradient(ellipse at 55% 45%,var(--bright) 0%,var(--blue) 35%,var(--deep) 75%,var(--navy) 100%)}
.tech-bg::after{content:"";position:absolute;inset:0;
  background-image:linear-gradient(rgba(120,190,255,.12) 1px,transparent 1px),linear-gradient(90deg,rgba(120,190,255,.12) 1px,transparent 1px);
  background-size:22px 22px}
.lorem{font-size:6.4px;line-height:9.4px;color:var(--ink);font-weight:500;text-align:justify;position:absolute}

/* cover slide */
.slide-cover{left:22px;top:25px;width:441px;height:311px}
.cover-title{position:absolute;left:73px;top:54px;font-size:33px;font-weight:900;letter-spacing:-.5px;
  background:linear-gradient(var(--title-top),#1c5bb8);-webkit-background-clip:text;background-clip:text;color:transparent}
.cover-rule{position:absolute;left:73px;top:91px;width:246px;height:1.5px;background:var(--cyan)}
.cover-text{position:absolute;left:73px;top:153px;width:246px;color:var(--white);font-size:9.4px;line-height:12.6px;font-weight:500;text-align:justify}

/* icons slide */
.slide-icons{left:714px;top:25px;width:440px;height:311px;background:var(--white)}
.icons-strip{position:absolute;left:0;top:0;width:127px;height:100%}
.strip-line{position:absolute;left:19px;top:20px;width:1.5px;height:120px;background:var(--white)}
.strip-title{position:absolute;left:30px;top:24px;color:var(--white);font-weight:900;font-size:37px;
  writing-mode:vertical-rl;transform:rotate(180deg);letter-spacing:1px;white-space:nowrap;height:300px;text-align:right}
.feature{position:absolute;width:78px;text-align:center}
.feature svg{display:block;margin:0 auto 6px}
.feature .lorem{position:static;text-align:justify}

/* two column slide */
.slide-columns{left:24px;top:367px;width:439px;height:311px}
.col-head{position:absolute;left:71px;top:26px;font-size:19px;font-weight:900;
  background:linear-gradient(var(--title-top),var(--title-bottom));-webkit-background-clip:text;background-clip:text;color:transparent}
.col-sub{position:absolute;left:71px;top:53px;font-size:9px;font-weight:800;color:var(--ink)}
.col-note{border-left:1.5px solid var(--ink);padding-left:4px}

/* stats slide */
.slide-stats{left:353px;top:230px;width:440px;height:311px;z-index:5}
.stat-value{position:absolute;width:130px;text-align:center;color:var(--white);font-weight:800;font-size:29px}
.stat-label{position:absolute;width:86px;text-align:center;color:var(--white);font-size:5px;line-height:8px;font-weight:500}

/* coin slide */
.slide-coins{left:714px;top:367px;width:440px;height:311px;background:var(--white)}
.coins-visual{position:absolute;left:0;top:0;width:100%;height:177px}
.coin-card{position:absolute;top:153px;width:96px;height:94px;background:var(--white);box-shadow:0 1px 4px rgba(0,0,0,.25);
  display:flex;align-items:center;justify-content:center}

/* brand + title */
.brand{position:absolute;left:499px;top:626px;width:200px;text-align:center;font-size:24px;font-weight:800;color:var(--bright)}
.brand-mark{display:inline-block;width:14px;height:14px;border-radius:50%;background:var(--bright);margin-right:8px;vertical-align:1px}
.headline{position:absolute;left:0;top:724px;width:1200px;text-align:center;font-size:67px;font-weight:900;letter-spacing:1px;line-height:1.1;
  background:linear-gradient(var(--title-top),var(--title-bottom));-webkit-background-clip:text;background-clip:text;color:transparent}
</style>
</head>
<body>

<section class="slide slide-cover">
  <div class="tech-bg" role="img" aria-label="Blaue Technologie-Szene mit Datennetz und Kurscharts"></div>
  <h1 class="cover-title">LOREM IPSUM</h1>
  <div class="cover-rule"></div>
  <p class="cover-text">Lorem ipsum dolor sit amet, consectetur adipiscing elit, sed do eiusmod tempor incididunt ut labore et dolore magna aliqua. Quis ipsum suspendisse ultrices gravida. Risus commodo viverra maecenas accumsan lacus vel facilisis.</p>
</section>

<section class="slide slide-icons">
  <div class="icons-strip tech-bg" role="img" aria-label="Blauer Hintergrund mit Kurscharts"></div>
  <div class="strip-line"></div>
  <div class="strip-title">LOREM IPSUM</div>

  <div class="feature" style="left:154px;top:55px">
    <svg width="44" height="42" viewBox="0 0 44 42"><polygon points="22,1 43,16 35,41 9,41 1,16" fill="#111"/><circle cx="22" cy="23" r="9" fill="none" stroke="#fff" stroke-width="1.3"/></svg>
    <p class="lorem">Lorem ipsum dolor sit amet, consectetur adipiscing elit, sed do eiusmod tempor incididunt ut labore et dolore</p>
  </div>
  <div class="feature" style="left:245px;top:55px">
    <svg width="44" height="42" viewBox="0 0 44 42"><polygon points="22,1 43,16 35,41 9,41 1,16" fill="#111"/><circle cx="22" cy="23" r="9" fill="none" stroke="#fff" stroke-width="1.3"/><line x1="13" y1="23" x2="31" y2="23" stroke="#fff" stroke-width="1.2"/></svg>
    <p class="lorem">Lorem ipsum dolor sit amet, consectetur adipiscing elit, sed do eiusmod tempor incididunt ut labore et dolore</p>
  </div>
  <div class="feature" style="left:336px;top:55px">
    <svg width="44" height="42" viewBox="0 0 44 42"><polygon points="22,1 43,16 35,41 9,41 1,16" fill="#111"/><rect x="15" y="20" width="14" height="11" rx="2" fill="none" stroke="#fff" stroke-width="1.3"/><path d="M18 20v-3a4 4 0 0 1 8 0v3" fill="none" stroke="#fff" stroke-width="1.3"/></svg>
    <p class="lorem">Lorem ipsum dolor sit amet, consectetur adipiscing elit, sed do eiusmod tempor incididunt ut labore et dolore</p>
  </div>
  <div class="feature" style="left:154px;top:157px">
    <svg width="44" height="42" viewBox="0 0 44 42"><polygon points="22,1 43,16 35,41 9,41 1,16" fill="#111"/><rect x="16" y="14" width="12" height="18" rx="2" fill="none" stroke="#fff" stroke-width="1.3"/></svg>
    <p class="lorem">Lorem ipsum dolor sit amet, consectetur adipiscing elit, sed do eiusmod tempor incididunt ut labore et dolore magna aliqua. Quis ipsum suspendisse ultrices gravida. Risus</p>
  </div>
  <div class="feature" style="left:245px;top:157px">
    <svg width="44" height="42" viewBox="0 0 44 42"><polygon points="22,1 43,16 35,41 9,41 1,16" fill="#111"/><rect x="13" y="17" width="18" height="13" rx="2" fill="none" stroke="#fff" stroke-width="1.3"/></svg>
    <p class="lorem">Lorem ipsum dolor sit amet, consectetur adipiscing elit, sed do eiusmod tempor incididunt ut labore et dolore magna aliqua. Quis ipsum suspendisse ultrices gravida. Risus</p>
  </div>
  <div class="feature" style="left:336px;top:157px">
    <svg width="44" height="42" viewBox="0 0 44 42"><polygon points="22,1 43,16 35,41 9,41 1,16" fill="#111"/><rect x="13" y="18" width="18" height="12" rx="2" fill="none" stroke="#fff" stroke-width="1.3"/><circle cx="19" cy="24" r="2.2" fill="#fff"/></svg>
    <p class="lorem">Lorem ipsum dolor sit amet, consectetur adipiscing elit, sed do eiusmod tempor incididunt ut labore et dolore magna aliqua. Quis ipsum suspendisse ultrices gravida. Risus</p>
  </div>
</section>

<section class="slide slide-columns">
  <div class="tech-bg" role="img" aria-label="Blaue Technologie-Szene mit Kurscharts"></div>
  <svg style="position:absolute;inset:0" width="439" height="311" viewBox="0 0 439 311">
    <polygon points="0,0 222,0 363,155 222,311 0,311" fill="#fff"/>
    <polygon points="0,0 155,153 0,311" fill="var(--navy)"/>
    <line x1="17" y1="32" x2="139" y2="153" stroke="#fff" stroke-width="1"/>
  </svg>
  <h2 class="col-head">LOREM IPSUM</h2>
  <div class="col-sub">LOREM IPSUM</div>
  <p class="lorem" style="left:158px;top:104px;width:86px;font-size:5.2px;line-height:7.5px">Lorem ipsum dolor sit amet, consectetur adipiscing elit, sed do eiusmod tempor incididunt ut labore et dolore magna aliqua. Quis ipsum suspendisse ultrices gravida. Risus commodo viverra maecenas accumsan lacus vel facilisis.</p>
  <p class="lorem" style="left:253px;top:104px;width:86px;font-size:5.2px;line-height:7.5px">Lorem ipsum dolor sit amet, consectetur adipiscing elit, sed do eiusmod tempor incididunt ut labore et dolore magna aliqua. Quis ipsum suspendisse ultrices gravida. Risus commodo viverra maecenas accumsan lacus vel facilisis.</p>
  <p class="lorem col-note" style="left:70px;top:241px;width:88px;font-size:5.2px;line-height:7.5px">Lorem ipsum dolor sit amet, consectetur adipiscing elit, sed do eiusmod tempor incididunt ut labore et dolore magna aliqua. Quis ipsum suspendisse ultrices gravida. Risus commodo viverra maecenas accumsan lacus vel facilisis.</p>
</section>

<section class="slide slide-coins">
  <div class="coins-visual tech-bg" role="img" aria-label="Leuchtendes Krypto-Münzsymbol aus Datennetz vor Kurscharts"></div>
  <div class="coin-card" style="left:18px"><svg width="68" height="68" viewBox="0 0 68 68"><circle cx="34" cy="34" r="32" fill="none" stroke="#111" stroke-width="2.5"/><circle cx="34" cy="34" r="26" fill="none" stroke="#111" stroke-width="2"/></svg></div>
  <div class="coin-card" style="left:169px"><svg width="68" height="68" viewBox="0 0 68 68"><circle cx="34" cy="34" r="32" fill="none" stroke="#111" stroke-width="2.5"/><circle cx="34" cy="34" r="26" fill="none" stroke="#111" stroke-width="2"/></svg></div>
  <div class="coin-card" style="left:320px"><svg width="68" height="68" viewBox="0 0 68 68"><circle cx="34" cy="34" r="32" fill="none" stroke="#111" stroke-width="2.5"/><circle cx="34" cy="34" r="26" fill="none" stroke="#111" stroke-width="2"/></svg></div>
  <p class="lorem" style="left:18px;top:266px;width:404px;font-size:6.1px;line-height:9.4px">Lorem ipsum dolor sit amet, consectetur adipiscing elit, sed do eiusmod tempor incididunt ut labore et dolore magna aliqua. Quis ipsum suspendisse ultrices gravida. Risus commodo viverra maecenas accumsan lacus vel facilisis. Lorem ipsum dolor sit amet, consectetur adipiscing elit, sed do eiusmod tempor incididunt ut labore et dolore magna aliqua. Quis ipsum suspendisse ultrices gravida. Risus com-</p>
</section>

<section class="slide slide-stats">
  <div class="tech-bg" role="img" aria-label="Blaue Technologie-Szene mit Kurscharts und Datennetz"></div>
  <svg style="position:absolute;inset:0" width="440" height="311" viewBox="0 0 440 311">
    <polygon points="86,0 440,0 440,311 185,311" fill="#fff"/>
    <circle cx="200" cy="86" r="65" fill="#000"/>
    <path d="M128 70 A73 73 0 0 1 273 86" fill="none" stroke="var(--cyan)" stroke-width="6"/>
    <circle cx="357" cy="86" r="65" fill="#000"/>
    <path d="M357 12 A74 74 0 0 1 362 160" fill="none" stroke="var(--cyan)" stroke-width="6"/>
  </svg>
  <div class="stat-value" style="left:135px;top:53px">50%</div>
  <div class="stat-label" style="left:157px;top:99px">Lorem ipsum dolor sit amet, consectetur adipiscing elit, sed do eiusmod tempor incididunt</div>
  <div class="stat-value" style="left:294px;top:53px">50%</div>
  <div class="stat-label" style="left:314px;top:99px">Lorem ipsum dolor sit amet, consectetur adipiscing elit, sed do eiusmod tempor incididunt</div>
  <p class="lorem" style="left:194px;top:187px;width:223px;font-size:6.5px;line-height:9.6px">Lorem ipsum dolor sit amet, consectetur adipiscing elit, sed do eiusmod tempor incididunt ut labore et dolore magna aliqua. Quis ipsum suspendisse ultrices gravida. Risus commodo viverra maecenas accumsan lacus vel facilisis. Lorem ipsum dolor sit amet, consectetur adipiscing elit, sed do eiusmod tempor incididunt ut labore et dolore magna aliqua. Quis ipsum suspendisse ultrices gravida. Risus commodo viverra maecenas accumsan lacus vel facilisis. Lorem ipsum dolor sit amet, consectetur adipiscing elit, sed do eiusmod tempor incididunt ut labore et dolore magna aliqua. Quis ipsum suspendisse ultrices gravida. Risus commodo viverra maecenas accumsan lacus vel facilisis. Lorem ipsum dolor sit amet, consectetur adipiscing elit, sed do eiusmod tempor incididunt ut</p>
</section>

<div class="brand"><span class="brand-mark"></span>Kranwerk</div>
<h1 class="headline">PRÄSENTATIONSVORLAGEN</h1>

</body>
</html>
```